Business card design for IT consulting company

Looking for a simple, modern, clean business card design.
Open to reworking our existing logo.

Attached is our current business cards which we do not like.
Ideally double sided with something simple on the back.
Rectangle / Horizonal only.
No rounded edges on the card.
White as the dominate color is preferred.

Target Market(s)

clients, legal, oil & gas, medical, professionals

Industry/Entity Type

IT, tech, consulting

Contact Information for Business Card

Name, Title, email, phone, cell, website

Font styles to use
Sans Serif

Requirements
Must have
• Clean design
Should not have
• loud colors or unusual fonts, etc

```html
<!DOCTYPE html>
<html lang="en">
<head>
<meta charset="UTF-8">
<title>Halvenrook Solutions – Business Card</title>
<link href="https://fonts.googleapis.com/css2?family=Montserrat:wght@500;700&family=Open+Sans:wght@400;600&display=swap" rel="stylesheet">
<style>
  :root {
    --stage: #2b2b2b;
    --card-white: #f7f7f6;
    --card-dark: #1e1e1e;
    --ink: #161616;
    --ink-light: #f2f2f2;
    --accent-yellow: #f4c430;
    --accent-blue: #4bb3e0;
    --accent-red: #e8445a;
    --accent-navy: #2b2a7a;
    --divider: #8a8a8a;
  }
  * { margin: 0; padding: 0; box-sizing: border-box; }
  html, body {
    width: 1200px; height: 750px; overflow: hidden;
    background: var(--stage);
  }
  .stage {
    width: 1200px; height: 750px;
    display: flex; align-items: center; justify-content: center; gap: 40px;
  }
  .card {
    width: 520px; height: 297px;
    position: relative;
    box-shadow: 0 10px 30px rgba(0,0,0,.45);
    overflow: hidden;
  }
  /* Front */
  .card--front {
    background: var(--card-white);
    display: flex; flex-direction: column; align-items: center; justify-content: center;
  }
  .brand {
    display: flex; align-items: center; gap: 14px;
  }
  .brand__square {
    width: 56px; height: 56px; border-radius: 9px;
    background: var(--accent-navy);
    flex-shrink: 0;
  }
  .brand__name {
    font-family: "Montserrat", sans-serif;
    font-weight: 700; font-size: 33px; letter-spacing: -0.5px;
    color: var(--ink); white-space: nowrap;
  }
  .front__url {
    margin-top: 28px;
    font-family: "Montserrat", sans-serif;
    font-weight: 700; font-size: 12px; letter-spacing: 4px;
    color: var(--ink);
  }
  /* Back */
  .card--back {
    background: var(--card-dark);
    display: flex; align-items: center;
    padding-left: 56px;
  }
  .back__brand {
    width: 170px;
    display: flex; flex-direction: column; align-items: center; gap: 12px;
  }
  .back__square {
    width: 110px; height: 110px; border-radius: 16px;
    background: var(--accent-blue);
  }
  .back__name {
    font-family: "Montserrat", sans-serif;
    font-weight: 700; font-size: 20px;
    color: var(--ink-light); white-space: nowrap;
  }
  .back__divider {
    width: 1px; height: 150px; background: var(--divider);
    margin: 0 24px 0 24px;
  }
  .contact__person {
    font-family: "Montserrat", sans-serif;
    font-weight: 700; font-size: 22px;
    color: var(--accent-yellow); line-height: 1.1;
  }
  .contact__title {
    font-family: "Open Sans", sans-serif;
    font-size: 12px; color: var(--accent-blue);
    margin-bottom: 10px;
  }
  .contact__list { list-style: none; }
  .contact__item {
    font-family: "Open Sans", sans-serif;
    font-size: 14px; color: var(--ink-light); line-height: 1.45;
    white-space: nowrap;
  }
  .contact__label {
    font-weight: 600; color: var(--accent-red);
    display: inline-block; width: 22px;
  }
</style>
</head>
<body>
<main class="stage">
  <section class="card card--front">
    <div class="brand">
      <span class="brand__square"></span>
      <span class="brand__name">Halvenrook Solutions</span>
    </div>
    <p class="front__url">www.halvenrook.com</p>
  </section>

  <section class="card card--back">
    <div class="back__brand">
      <span class="back__square"></span>
      <span class="back__name">Halvenrook</span>
    </div>
    <span class="back__divider"></span>
    <div class="contact">
      <p class="contact__person">Daniel Hart</p>
      <p class="contact__title">IT Consultant</p>
      <ul class="contact__list">
        <li class="contact__item"><span class="contact__label">P:</span>(800) 555-0142</li>
        <li class="contact__item"><span class="contact__label">C:</span>(604) 555-0187</li>
        <li class="contact__item"><span class="contact__label">E:</span>d.hart@halvenrook.ca</li>
        <li class="contact__item"><span class="contact__label">W:</span>www.halvenrook.ca</li>
      </ul>
    </div>
  </section>
</main>
</body>
</html>
```